Rodeo Sponsor booklet

I am needing a multi page handout made for potential sponsors for our Tamsley Flats Rodeo. I have attached our previous one and our 2025 poster that we would like it to flow similarly. You will see on the "example of 2025" the markup we would like changed and of course new front cover etc.
These are the following uploads
2025 Tamsley Flats Rodeo -5.jpg this is the new 2025 poster match look and feel
Rodeo Brochure R-3.pdf. this is 2024 sponsor brochure I need the same idea with a different look and feel but match the above poster
This is the new information that is needed on the new 2025 brochure with changes that I would like made. it can have what ever look and feel I was just playing around. nothing about it needs to be similar to this but all information does need to be in the document
The rest are photos we like and you can use which ever I just like the look and feel of the 2024 one so want that same feeling!

```html
<!DOCTYPE html>
<html lang="en">
<head>
<meta charset="utf-8">
<title>Tamsley Flats Rodeo – Sponsor Booklet</title>
<link rel="stylesheet" href="https://fonts.googleapis.com/css2?family=Anton&family=League+Gothic&family=Oswald:wght@500;600&family=Jost:wght@300;400&display=swap">
<style>
  :root{
    --paper:#ece4d6;
    --paper-light:#f1ece3;
    --brown-dark:#4a3328;
    --brown:#5b4032;
    --tan:#d9a062;
    --tan-deep:#c27b3a;
    --tag:#c8955f;
    --card:#f2d9b5;
    --diamond:#f0a33c;
    --ink:#3a2e26;
    --night:#2f2c2a;
    --cream:#e6e0d8;
    --accent:#e59a4c;
    --star:#efcf86;
  }
  *{box-sizing:border-box;margin:0;padding:0}
  html,body{width:1200px;height:640px;overflow:hidden;background:#fff}
  body{position:relative;font-family:"Jost",sans-serif}

  .page{position:absolute;top:110px;height:420px;overflow:hidden;box-shadow:0 6px 14px rgba(0,0,0,.12)}

  /* ---------- Cover ---------- */
  .cover{left:60px;width:330px;background:linear-gradient(160deg,#efe8dc,#e4dacb)}
  .cover__badge{position:absolute;left:15px;top:0;width:89px;height:88px;background:var(--brown-dark);
    display:flex;flex-direction:column;align-items:center;justify-content:center;gap:6px;
    color:var(--paper);font-family:"Oswald",sans-serif;font-weight:600;font-size:11px;line-height:1.15;text-align:center;text-transform:uppercase}
  .cover__badge-dot{width:10px;height:10px;border-radius:50%;background:var(--paper)}
  .cover__backdrop{position:absolute;left:135px;top:0;width:195px;height:180px;
    background:radial-gradient(ellipse at 45% 45%,rgba(200,185,165,.55),rgba(236,228,214,0) 70%)}
  .cover__headline{position:absolute;left:24px;top:98px;font-family:"Anton",sans-serif;font-size:82px;line-height:1;
    color:var(--brown);text-shadow:4px 4px 0 rgba(91,64,50,.25);white-space:nowrap}
  .cover__photo{position:absolute;left:100px;top:135px;width:230px;height:240px;
    background:radial-gradient(ellipse at 55% 55%,#4a2f20,#6b4632 45%,rgba(107,70,50,0) 72%);
    clip-path:polygon(20% 30%,45% 0,62% 10%,100% 5%,100% 60%,75% 75%,40% 100%,15% 70%,0 45%)}
  .cover__strip{position:absolute;left:15px;top:195px;width:135px;height:32px;background:#b98e63;
    font-family:"Anton",sans-serif;font-size:25px;line-height:32px;color:#f0d2a6;padding-left:14px;white-space:nowrap}
  .cover__tough{position:absolute;top:305px;font-family:"Anton",sans-serif;font-size:44px;color:var(--tan);line-height:1;white-space:nowrap}
  .cover__tough--a{left:8px}
  .cover__tough--b{left:195px}
  .cover__tagline{position:absolute;left:98px;top:372px;font-family:"Oswald",sans-serif;font-weight:600;font-size:16px;line-height:1.2;color:#c98740;white-space:nowrap}
  .star{position:absolute;fill:var(--star)}

  /* ---------- Spread left ---------- */
  .levels{left:500px;width:320px;background:var(--paper-light)}
  .levels__header{position:absolute;left:19px;top:16px;display:flex;align-items:center;gap:10px}
  .levels__title{font-family:"League Gothic",sans-serif;font-weight:400;font-size:32px;line-height:1;color:#2a2420;letter-spacing:.3px;white-space:nowrap}
  .levels__star{width:30px;height:30px;fill:var(--star);flex:none}
  .levels__divider{position:absolute;left:161px;width:0;border-left:1px dotted #8a7a6a}
  .tier{position:absolute;background:var(--card)}
  .tier__head{position:absolute;left:6px;top:26px;display:flex;align-items:center;gap:3px;color:var(--tan-deep)}
  .tier__num{font-family:"Anton",sans-serif;font-size:22px;line-height:1}
  .tier__name{font-family:"Oswald",sans-serif;font-weight:600;font-size:10px;line-height:1.1;text-transform:uppercase}
  .tier__price{position:absolute;right:-6px;top:6px;width:78px;height:18px;background:var(--tag);transform:rotate(-2deg);
    font-family:"Anton",sans-serif;font-size:13px;line-height:18px;color:#fff;text-align:center}
  .tier__perks{position:absolute;left:10px;right:8px;list-style:none;font-size:5.6px;line-height:1.35;color:var(--ink)}
  .tier__perks li{position:relative;padding-left:5px;margin-bottom:7px}
  .tier__perks li::before{content:"•";position:absolute;left:0}
  .tier__perks--tight li{margin-bottom:5px}
  .tier--diamond{background:var(--diamond)}
  .tier--diamond .tier__head{top:8px;left:10px;color:#b8561a}
  .tier--diamond .tier__perks{left:30px;top:30px;right:62px}
  .tier--diamond .tier__perks li{margin-bottom:1px}
  .tier__scene{position:absolute;right:8px;bottom:0;width:56px;height:30px;
    background:linear-gradient(to top,#5a3a22,#c98a55 55%,#f6c9b3)}

  /* ---------- Spread right ---------- */
  .story{left:820px;width:320px;background:var(--night)}
  .story__collage{position:absolute;left:118px;top:0;width:202px;height:420px}
  .story__title{position:absolute;left:14px;top:56px;width:120px;text-align:center;font-family:"Anton",sans-serif;font-weight:400;font-size:24px;line-height:1.2;letter-spacing:2px;color:#fff}
  .story__quote{position:absolute;left:14px;top:96px;width:120px;text-align:center;font-family:"Oswald",sans-serif;font-weight:500;font-size:12.5px;line-height:1.35;color:#fff}
  .story__author{position:absolute;left:14px;top:166px;width:120px;text-align:center;font-weight:300;font-size:13px;color:var(--accent)}
  .story__rule{position:absolute;left:22px;width:100px;height:1px;background:#8b847c}
  .story__body{position:absolute;left:20px;top:205px;width:110px;font-size:5.8px;line-height:1.6;color:var(--cream)}
</style>
</head>
<body>

<!-- Cover -->
<section class="page cover">
  <div class="cover__backdrop" role="img" aria-label="Faded photo of a cowboy in a hat"></div>
  <div class="cover__badge"><span class="cover__badge-dot"></span><span>Tamsley Flats<br>Rodeo</span></div>
  <svg class="star" style="left:272px;top:64px;width:56px;height:56px" viewBox="0 0 24 24"><polygon points="12,1 15,9 23,9 16.5,14 19,22 12,17 5,22 7.5,14 1,9 9,9"/></svg>
  <div class="cover__headline">COWBOY</div>
  <div class="cover__strip">IS A BREED</div>
  <svg class="star" style="left:132px;top:198px;width:34px;height:34px" viewBox="0 0 24 24"><polygon points="12,1 15,9 23,9 16.5,14 19,22 12,17 5,22 7.5,14 1,9 9,9"/></svg>
  <div class="cover__photo" role="img" aria-label="Photo of a bull rider on a bucking bull"></div>
  <div class="cover__tough cover__tough--a">TOUGHER</div>
  <div class="cover__tough cover__tough--b">THAN</div>
  <div class="cover__tagline">NAILS &amp; STRONGER THAN STEEL</div>
</section>

<!-- Sponsorship levels -->
<section class="page levels">
  <header class="levels__header">
    <h1 class="levels__title">BASE SPONSORSHIP LEVELS</h1>
    <svg class="levels__star" viewBox="0 0 24 24"><polygon points="12,1 15,9 23,9 16.5,14 19,22 12,17 5,22 7.5,14 1,9 9,9"/></svg>
  </header>

  <div class="levels__divider" style="top:70px;height:140px"></div>
  <div class="levels__divider" style="top:225px;height:105px"></div>

  <article class="tier" style="left:19px;top:68px;width:123px;height:144px">
    <div class="tier__price">$1,000</div>
    <div class="tier__head"><span class="tier__num">1</span><span class="tier__name">Bronze<br>Supporter</span></div>
    <ul class="tier__perks" style="top:58px">
      <li>Company name listed in the event program.</li>
      <li>Social media mention on all rodeo related pages.</li>
      <li>Small logo display on the event's main digital screen.</li>
      <li>4 Single Day Passes to the rodeo.</li>
    </ul>
  </article>

  <article class="tier" style="left:181px;top:68px;width:123px;height:144px">
    <div class="tier__price">$3,000</div>
    <div class="tier__head"><span class="tier__num">2</span><span class="tier__name">Silver<br>Supporter</span></div>
    <ul class="tier__perks" style="top:58px">
      <li>Includes all Bronze Supporter benefits.</li>
      <li>Company logo on the event website.</li>
      <li>Company banner displayed at the event (provided by the rodeo).</li>
      <li>6 Single Day Passes to the rodeo.</li>
    </ul>
  </article>

  <article class="tier" style="left:19px;top:218px;width:123px;height:114px">
    <div class="tier__price">$4,500</div>
    <div class="tier__head"><span class="tier__num">3</span><span class="tier__name">Gold<br>Supporter</span></div>
    <ul class="tier__perks" style="top:56px">
      <li>Includes all Silver Sponsor benefits.</li>
      <li>Medium-sized banner at the event (provided by the rodeo).</li>
      <li>6 Weekend Passes to the rodeo.</li>
    </ul>
  </article>

  <article class="tier" style="left:181px;top:218px;width:123px;height:114px">
    <div class="tier__price">$5,500</div>
    <div class="tier__head"><span class="tier__num">4</span><span class="tier__name">Platinum<br>Supporter</span></div>
    <ul class="tier__perks tier__perks--tight" style="top:54px">
      <li>Includes all Bronze Sponsor benefits.</li>
      <li>Company logo on the event website.</li>
      <li>Company banner displayed at the event (provided by the rodeo).</li>
      <li>6 Weekend passes with VIP seating to the rodeo.</li>
    </ul>
  </article>

  <article class="tier tier--diamond" style="left:19px;top:336px;width:286px;height:84px">
    <div class="tier__price" style="top:8px">$8,500</div>
    <div class="tier__head"><span class="tier__num">5</span><span class="tier__name">Diamond Supporter</span></div>
    <ul class="tier__perks">
      <li>Includes all Platinum Contributor benefits.</li>
      <li>Large banner in a prime location at the event (provided by the rodeo).</li>
      <li>Exclusive 2 VIP parking spots, 12 weekend VIP Passes to the Rodeo.</li>
      <li>Option to provide short Commercial for your company.</li>
      <li>A banner on one of the 6 chutes or main gates used in the arena.</li>
    </ul>
    <div class="tier__scene" role="img" aria-label="Illustration of riders on horseback at sunset"></div>
  </article>
</section>

<!-- Story page -->
<section class="page story">
  <svg class="story__collage" viewBox="0 0 202 420" role="img" aria-label="Collage of rodeo photos: steer wrestling, bronc riding and a bucking horse">
    <defs>
      <linearGradient id="dust" x1="0" y1="0" x2="1" y2="1">
        <stop offset="0" stop-color="#8a6a4c"/><stop offset="1" stop-color="#5a3f2c"/>
      </linearGradient>
      <linearGradient id="arena" x1="0" y1="0" x2="1" y2="1">
        <stop offset="0" stop-color="#9a7a5a"/><stop offset="1" stop-color="#6b4a33"/>
      </linearGradient>
    </defs>
    <polygon points="40,55 80,5 202,5 202,110 60,150 20,115" fill="url(#dust)"/>
    <polygon points="60,165 202,118 202,285 60,245" fill="url(#arena)"/>
    <polygon points="20,300 60,258 202,300 202,418 80,418 30,360" fill="url(#dust)"/>
    <circle cx="-10" cy="210" r="85" fill="#2f2c2a"/>
  </svg>

  <h2 class="story__title">COURAGE</h2>
  <p class="story__quote">is being scared<br>to death and<br>saddling up<br>anyway</p>
  <p class="story__author">Hank Calloway</p>
  <div class="story__rule" style="top:190px"></div>
  <p class="story__body">As we enthusiastically prepare for the 2024 Tamsley Flats Rodeo at the Tamsley Flats Community Rodeo grounds, we are thrilled to continue the successful format from last year. This year, we're once again expanding to a 3-day family event, maintaining our exciting Friday afternoon Gymkhana in the lineup. Join us as we continue the beloved rodeo tradition, a highlight of our community for over 35 years, bringing joy and excitement to families and rodeo enthusiasts alike.</p>
  <div class="story__rule" style="top:345px"></div>
</section>

</body>
</html>
```